CBD PATCHES

Design creation of my CBD patch box.
Product must look Pharamaceutical grade.
Colours need to look pharmaceutical (green/white/maybe a bit of blue).
Text: Cannabidiol (CBD) Self-curing adhesive Polyethylene backing sheet.
Apply one patch to a smooth are of skin. Each patch can be worn for up to 24 hours. Apply subsequent patches to different areas to allow the skin to breathe between uses.
Do not apply to broken or irritable skin. Consult a doctor if you are taking medications or have medical conditions before using this or any other supplement. Do not use if you are pregnant or breastfeeding.
Store in a cool, dry place out of direct sunlight. Stable for three years. Once opened, use within 12 months.

```html
<!DOCTYPE html>
<html lang="en">
<head>
<meta charset="UTF-8">
<title>Cannabidiol CBD Patch Box</title>
<link href="https://fonts.googleapis.com/css2?family=Poppins:wght@400;500;700;800&display=swap" rel="stylesheet">
<style>
  :root {
    --stage: #7f8a1d;
    --lime: #b6d647;
    --lime-deep: #8fae3a;
    --paper: #ffffff;
    --ink: #161616;
    --leaf-light: #c9df7a;
    --leaf-dark: #8fb33a;
  }
  * { box-sizing: border-box; margin: 0; padding: 0; }
  html, body { width: 1200px; height: 1000px; overflow: hidden; }
  body {
    background: var(--stage);
    font-family: "Poppins", sans-serif;
    color: var(--ink);
    position: relative;
  }
  .panel {
    position: absolute;
    top: 290px;
    width: 410px;
    height: 440px;
    background: var(--paper);
    overflow: hidden;
  }
  .panel--info { left: 160px; }
  .panel--front { left: 630px; }

  .band { position: absolute; left: 0; width: 100%; display: block; }
  .band--top { top: 0; height: 60px; }
  .band--bottom { bottom: 0; }

  .info-copy {
    position: absolute;
    left: 26px; right: 26px; top: 78px;
    font-size: 15.5px;
    line-height: 1.42;
    text-align: justify;
  }
  .info-copy p + p { margin-top: 22px; }

  .storage {
    position: absolute;
    left: 26px; right: 26px; bottom: 22px;
    font-size: 15.5px;
    line-height: 1.42;
    text-align: justify;
  }

  .brand {
    position: absolute;
    left: 34px; top: 86px;
    display: flex; flex-direction: column; align-items: center; gap: 6px;
  }
  .brand__mark {
    width: 50px; height: 50px; border-radius: 50%;
    background: var(--lime);
  }
  .brand__name {
    font-size: 10px; font-weight: 700; color: var(--lime-deep);
    letter-spacing: 0.5px; line-height: 1.1; text-align: center;
  }
  .brand__name small { display: block; font-size: 6px; }

  .product-title {
    position: absolute;
    left: 34px; top: 196px;
    font-size: 34px; font-weight: 700; line-height: 1.25;
    color: var(--lime);
  }
  .product-specs {
    position: absolute;
    left: 36px; top: 300px;
    font-size: 11.5px; line-height: 1.65;
  }
  .leaf-art {
    position: absolute;
    right: 18px; top: 222px;
    width: 118px; height: 136px;
    border-radius: 50% 50% 40% 40%;
    background: radial-gradient(circle at 50% 45%, var(--leaf-light), var(--leaf-dark));
    opacity: 0.9;
  }
</style>
</head>
<body>

  <section class="panel panel--info">
    <svg class="band band--top" viewBox="0 0 410 60" preserveAspectRatio="none" aria-hidden="true">
      <path d="M0 0 H410 V40 Q200 30 0 60 Z" fill="var(--lime)"/>
    </svg>
    <div class="info-copy">
      <p>Apply one patch to a smooth are of skin. Each patch can be worn for up to 24 hours. Apply subsequent patches to different areas to allow the skin to breathe between uses.</p>
      <p>Do not apply to broken or irritable skin. Consult a doctor if you are taking medications or have medical conditions before using this or any other supplement. Do not use if you are pregnant or breastfeeding.</p>
    </div>
    <svg class="band band--bottom" style="height:120px" viewBox="0 0 410 120" preserveAspectRatio="none" aria-hidden="true">
      <path d="M0 12 Q200 0 410 4 V120 H0 Z" fill="var(--lime)"/>
    </svg>
    <p class="storage">Store in a cool, dry place out of direct sunlight. Stable for three years. Once opened, use within 12 months.</p>
  </section>

  <section class="panel panel--front">
    <svg class="band band--top" viewBox="0 0 410 60" preserveAspectRatio="none" aria-hidden="true">
      <path d="M0 0 H410 V20 Q200 50 0 60 Z" fill="var(--lime)"/>
    </svg>
    <div class="brand">
      <span class="brand__mark"></span>
      <span class="brand__name">VERDALEAF<small>CBD PATCHES</small></span>
    </div>
    <h1 class="product-title">Cannabidiol<br>(CBD)</h1>
    <p class="product-specs">Self-curing adhesive<br>Polyethylene backing sheet</p>
    <div class="leaf-art" role="img" aria-label="Green cannabis leaf illustration"></div>
    <svg class="band band--bottom" style="height:120px" viewBox="0 0 410 120" preserveAspectRatio="none" aria-hidden="true">
      <path d="M0 90 Q260 75 410 20 V120 H0 Z" fill="var(--lime)"/>
    </svg>
  </section>

</body>
</html>
```